We need a logo for our business which is a dental clinic (i.e. dentistry).
We would lilke designs using the colour blue, green and black incorporating the words Corvasta Dental, possibly a smile or a tooth image can be considered for incorporation in the logo.

Industry/Entity Type

Dental

```html
<!DOCTYPE html>
<html lang="en">
<head>
<meta charset="utf-8">
<title>Corvasta Dental – Business Card</title>
<link rel="stylesheet" href="https://fonts.googleapis.com/css2?family=Source+Sans+3:wght@400;600&display=swap">
<style>
  :root {
    --backdrop: #939393;
    --card: #022a3d;
    --card-edge: #01090e;
    --accent: #1a9ad6;
    --accent-deep: #0b6c9c;
    --ink: #ffffff;
    --web: #1a8bc4;
  }
  * { margin: 0; padding: 0; box-sizing: border-box; }
  html, body {
    width: 1200px; height: 770px; overflow: hidden;
    background: var(--backdrop);
    font-family: "Source Sans 3", sans-serif;
  }
  .card {
    position: absolute; left: 250px; top: 179px;
    width: 712px; height: 416px;
    background: var(--card);
    overflow: hidden;
  }
  .brand {
    position: absolute; left: 28px; top: 36px;
    display: flex; align-items: center; gap: 14px;
  }
  .brand-dot {
    width: 30px; height: 30px; border-radius: 50%;
    background: var(--accent);
  }
  .brand-name {
    color: var(--accent);
    font-weight: 600; font-size: 34px;
    letter-spacing: 1px; line-height: 1;
  }
  .person { position: absolute; left: 44px; top: 199px; }
  .person-name { color: var(--ink); font-weight: 600; font-size: 20px; line-height: 1.2; }
  .person-role { color: var(--accent); font-size: 17px; line-height: 1.2; }
  .contacts {
    position: absolute; left: 368px; top: 204px;
    list-style: none; color: var(--ink); font-size: 16.5px;
  }
  .contact { display: flex; align-items: flex-start; height: 30px; }
  .contact.address { margin-top: 12px; line-height: 1.15; }
  .contact svg { width: 18px; height: 18px; flex: none; margin-right: 14px; margin-top: 1px; fill: var(--accent); }
  .footer { position: absolute; left: 0; bottom: 0; width: 712px; height: 40px; }
  .website {
    position: absolute; left: 48px; bottom: 8px;
    color: var(--web); font-size: 17px;
  }
</style>
</head>
<body>
  <main class="card">
    <div class="brand">
      <span class="brand-dot"></span>
      <span class="brand-name">Corvasta Dental</span>
    </div>

    <div class="person">
      <p class="person-name">Daniel Hargrove</p>
      <p class="person-role">President</p>
    </div>

    <ul class="contacts">
      <li class="contact">
        <svg viewBox="0 0 18 18"><rect x="1" y="1" width="16" height="16" rx="3"/><path d="M6 4c1 0 2 2 2 3s-1 1-1 1 1 3 3 3c0 0 0-1 1-1s3 1 3 2-1 2-2 2C8 14 4 10 4 6c0-1 1-2 2-2z" fill="#022a3d"/></svg>
        <span>+254 5710 38846</span>
      </li>
      <li class="contact">
        <svg viewBox="0 0 18 18"><path d="M1 7c0-3 16-3 16 0v1h-4V6H5v2H1z"/><path d="M4 9l2-2h6l2 2v6H4z"/><circle cx="9" cy="11.5" r="1.8" fill="#022a3d"/></svg>
        <span>+542 617 2093</span>
      </li>
      <li class="contact">
        <svg viewBox="0 0 18 18"><rect x="1" y="4" width="16" height="11"/><path d="M1 4l8 6 8-6" fill="none" stroke="#022a3d" stroke-width="1.4"/></svg>
        <span>info@corvasta.com</span>
      </li>
      <li class="contact address">
        <svg viewBox="0 0 18 18"><path d="M9 1a5 5 0 0 1 5 5c0 4-5 11-5 11S4 10 4 6a5 5 0 0 1 5-5z"/><circle cx="9" cy="6" r="1.8" fill="#022a3d"/></svg>
        <span>2180 Lakeview park road,<br>Portland, OR 97205</span>
      </li>
    </ul>

    <svg class="footer" viewBox="0 0 712 40" preserveAspectRatio="none">
      <path d="M0 0H300Q306 0 309 8L311 12Q313 16 320 16H712V40H0z" fill="var(--card-edge)"/>
      <path d="M310 9H712V17H318Q312 17 310 9z" fill="var(--accent)"/>
      <path d="M312 14H712V18H320Q314 18 312 14z" fill="var(--accent-deep)"/>
    </svg>
    <span class="website">www.corvasta.com</span>
  </main>
</body>
</html>
```